Farmers Market Banner for a Local Producer

I am looking for a design that incorporates my logo and grabs the attention of people quickly walking by. We are growers of natural and heirloom garlic, beans and herbs. Our focus is on quality, uniqueness and honesty. Some words that have been effective for us are: heirloom, pesticide - free, local, and family farm.
We would like to see the colors of the logo in the banner, but 1 additional color if needed is fine.
Updates

We have almost decided on our final version. Another few days should do it.

Target Market(s)

Primarily female aged 25-55 that is looking for a connection with the food they eat. Quality and the growing methods are most important to them and they are open to trying new varieties of food.

Industry/Entity Type

Pesticide

Requirements
Must have
• Our location ( Maple Ridge, British Columbia ). It should measure approx 9 feet long by 12 - 18 inches wide. This is going to be attached to the market stall canopy, either on the front or inside at the back. You are best to see one of these 10 feet by 10 feet canopies first ( Quikpop or Tarvona canopies or Brimlo canopy)
Nice to have
• We like the look and feel of our logo. This should be echoed in the banner design.
Should not have
• Cartoon art is to be avoided please.

```html
<!DOCTYPE html>
<html lang="en">
<head>
<meta charset="utf-8">
<title>Fieldrow Farm – Market Banner</title>
<link rel="stylesheet" href="https://fonts.googleapis.com/css2?family=Lato:wght@400;700;900&family=Questrial&display=swap">
<style>
  :root {
    --ink: #000000;
    --paper: #ffffff;
    --leaf: #a2c33a;
    --lime: #c8dc36;
    --strip: #8db742;
    --strip-text: #132009;
    --bean: #b33660;
    --bean-light: #d9879c;
    --wood: #8a8782;
    --garlic: #ece4dc;
    --stem: #a9c98a;
    --pod: #4a9a2a;
    --pod-deep: #2f7a1c;
  }
  * { box-sizing: border-box; margin: 0; padding: 0; }
  html, body { width: 1200px; height: 458px; overflow: hidden; background: var(--paper); }
  body { font-family: "Lato", sans-serif; position: relative; }

  .banner {
    position: absolute; left: 0; width: 1200px; height: 200px;
    background: var(--ink); overflow: hidden;
  }
  .banner--primary { top: 0; }
  .banner--alt { top: 258px; }

  .brand__mark {
    position: absolute; left: 20px; top: 10px; width: 102px; height: 102px;
    border-radius: 50%; border: 6px solid var(--leaf);
  }
  .brand__name {
    position: absolute; right: 678px; top: 14px;
    font-family: "Lato", sans-serif; font-weight: 900; font-size: 47px;
    letter-spacing: -1.5px; text-transform: uppercase;
    color: var(--leaf); line-height: 1; white-space: nowrap;
  }
  .brand__tagline {
    position: absolute; left: 190px; top: 64px;
    font-family: "Questrial", sans-serif; font-size: 38px; color: var(--paper);
    line-height: 1; white-space: nowrap; letter-spacing: -0.5px;
  }
  .brand__tagline em { font-style: normal; color: var(--leaf); }
  .banner--alt .brand__tagline em { color: var(--paper); }

  .location {
    position: absolute; left: 62px; top: 127px; width: 416px; height: 60px;
    border: 4px solid var(--paper); border-radius: 30px; background: var(--lime);
    display: flex; align-items: center; justify-content: center;
    font-weight: 700; font-size: 25px; letter-spacing: -0.3px; color: var(--ink);
  }

  .produce-photo {
    position: absolute; left: 541px; top: 0; width: 659px; height: 172px;
    background:
      linear-gradient(180deg, rgba(0,0,0,0) 60%, rgba(60,50,40,0.25) 100%),
      linear-gradient(90deg, var(--bean) 0%, var(--bean-light) 18%, var(--wood) 27%, var(--garlic) 36%, #e6d6df 52%, var(--garlic) 62%, var(--stem) 72%, var(--pod) 82%, var(--pod-deep) 100%);
  }

  .claim {
    position: absolute; left: 541px; top: 172px; width: 659px; height: 28px;
    background: var(--strip); padding-left: 19px;
    display: flex; align-items: center;
    font-weight: 700; font-size: 19px; color: var(--strip-text); white-space: nowrap;
  }
  .claim__lead { color: var(--paper); margin-right: 6px; }
  .banner--alt .claim { color: var(--paper); }
</style>
</head>
<body>

<section class="banner banner--primary">
  <span class="brand__mark"></span>
  <span class="brand__name">Fieldrow Farm</span>
  <span class="brand__tagline">grown <em>for</em> flavour</span>
  <div class="location">Maple Ridge, British Columbia</div>
  <div class="produce-photo" role="img" aria-label="Photo of speckled heirloom beans, fresh garlic bulbs and green bean pods"></div>
  <p class="claim"><span class="claim__lead">pesticide-free</span> heirloom varieties of garlic, beans, and more!</p>
</section>

<section class="banner banner--alt">
  <span class="brand__mark"></span>
  <span class="brand__name">Fieldrow Farm</span>
  <span class="brand__tagline">grown <em>for</em> flavour</span>
  <div class="location">Maple Ridge, British Columbia</div>
  <div class="produce-photo" role="img" aria-label="Photo of speckled heirloom beans, fresh garlic bulbs and green bean pods"></div>
  <p class="claim"><span class="claim__lead">pesticide-free</span> heirloom varieties of garlic, beans, and more!</p>
</section>

</body>
</html>
```